Brivanta.com the Free Online Tutorial Needs a New Web Design

We need a new web design for our existing website, Brivanta.com. We provide a Free Online Tutorial of any code, like HTML, CSS, PHP, Jquery, javascript etc, including online editor.
We would like to see designs that interesting, simple, interactive, and be a very comfortable place to read in a long time.
We need 2 pages design for:
1. Home Page (http://brivanta.com) and
2. Listing Page (http://brivanta.com/tutorial/833/sql/sql-basics/sql-and-or-operator.html)
For Listing Page We need nice "Left Menu" at left side and Content Page (min 728px) at right side.
I need File PSD and/or Vector Only, without HTML code.
Online
2 page

```html
<!DOCTYPE html>
<html lang="en">
<head>
<meta charset="utf-8">
<title>Brivanta — A place for learning and trying of any code</title>
<link href="https://fonts.googleapis.com/css2?family=Lato:wght@300;400;700;900&family=Dancing+Script:wght@600&display=swap" rel="stylesheet">
<style>
  :root {
    --ink: #2c2c2c;
    --muted: #555b61;
    --white: #ffffff;
    --hero-top: #3d4a57;
    --hero-bottom: #151b22;
    --band: #e6e8ea;
    --html: #e6c566;
    --css: #e07838;
    --js: #c02a4b;
    --php: #6b2338;
    --sql: #4e7e79;
    --navy: #2b3641;
    --navy-line: #3a4652;
    --red: #e0513c;
    --green: #2bb673;
    --blue: #3d84c4;
    --dark-btn: #2b3641;
    --footer: #333537;
    --footer-bar: #242526;
    --footer-text: #c9cbcd;
    --teal: #2cc3a0;
  }
  * { box-sizing: border-box; margin: 0; padding: 0; }
  html, body { width: 1200px; height: 2632px; overflow: hidden; }
  body { font-family: "Lato", Helvetica, Arial, sans-serif; color: var(--ink); background: var(--white); position: relative; }
  section, header, footer { position: absolute; left: 0; width: 1200px; }

  /* Hero */
  .hero { top: 0; height: 472px; overflow: hidden; }
  .hero-photo { position: absolute; inset: 0; background: linear-gradient(180deg, var(--hero-top) 0%, #26303a 55%, var(--hero-bottom) 100%); }
  .brand { position: absolute; left: 40px; top: 26px; display: flex; align-items: center; gap: 12px; color: var(--white); font-weight: 700; font-size: 30px; }
  .brand-mark { width: 26px; height: 26px; background: var(--teal); }
  .nav { position: absolute; right: 48px; top: 30px; display: flex; gap: 38px; list-style: none; }
  .nav li { color: var(--white); font-size: 17px; font-weight: 700; letter-spacing: 1px; padding-bottom: 8px; }
  .nav li.active { border-bottom: 3px solid var(--white); }
  .hero-title { position: absolute; top: 200px; width: 100%; text-align: center; color: var(--white); font-weight: 900; font-size: 50px; line-height: 60px; letter-spacing: 1px; }
  .btn { display: inline-block; color: var(--white); font-weight: 700; font-size: 20px; letter-spacing: 1px; text-align: center; line-height: 58px; height: 58px; }
  .hero .btn { position: absolute; top: 354px; left: 480px; width: 240px; background: var(--blue); }

  /* Tiles */
  .tiles { top: 472px; height: 368px; background: var(--band); }
  .tile { position: absolute; top: 46px; width: 216px; height: 276px; color: var(--white); clip-path: polygon(0 0, 82% 0, 100% 12%, 100% 100%, 0 100%); }
  .tile-icon { position: absolute; left: 58px; top: 44px; width: 100px; height: 100px; background: rgba(255,255,255,0.18); display: flex; align-items: center; justify-content: center; font-size: 32px; font-weight: 700; }
  .tile-label { position: absolute; left: 0; right: 0; bottom: 40px; text-align: center; font-size: 30px; font-weight: 700; letter-spacing: 1px; }
  .html { left: 50px; background: var(--html); }
  .css { left: 272px; background: var(--css); }
  .js { left: 494px; background: var(--js); }
  .php { left: 716px; background: var(--php); }
  .sql { left: 938px; background: var(--sql); }
  .tiles .arrow { position: absolute; top: 170px; }
  .arrow.prev { left: 12px; }
  .arrow.next { right: 12px; }

  /* Welcome */
  .welcome { top: 840px; height: 360px; }
  .laptop-area { position: absolute; left: 118px; top: 56px; width: 330px; height: 236px; border-radius: 10px; background: linear-gradient(180deg, #3a3e44 0%, #25282c 82%, #c4c7ca 86%, #e2e4e6 100%); }
  .welcome h2 { position: absolute; left: 600px; top: 78px; font-size: 44px; font-weight: 300; letter-spacing: 1px; }
  .welcome h2 b { font-weight: 900; }
  .welcome p { position: absolute; left: 600px; top: 150px; width: 500px; font-size: 19px; line-height: 28px; color: var(--muted); }
  .welcome .btn { position: absolute; left: 600px; top: 266px; width: 320px; background: var(--dark-btn); font-size: 18px; }

  /* Learn then practice */
  .learn { top: 1200px; height: 500px; background: var(--navy); color: var(--white); }
  .learn h2 { position: absolute; top: 76px; font-size: 64px; font-weight: 900; letter-spacing: 2px; }
  .learn .left-title { left: 190px; }
  .learn .right-title { left: 742px; }
  .then { position: absolute; left: 560px; top: 82px; font-family: "Dancing Script", cursive; font-size: 40px; color: #5d7b92; }
  .then-line { position: absolute; top: 118px; height: 1px; background: var(--navy-line); }
  .learn p { position: absolute; top: 190px; width: 400px; font-size: 19px; line-height: 28px; text-align: center; color: #e4e7ea; }
  .learn .left-copy { left: 100px; }
  .learn .right-copy { left: 700px; }
  .learn .btn { position: absolute; top: 322px; width: 300px; }
  .learn .red { left: 150px; background: var(--red); }
  .learn .green { left: 750px; background: var(--green); }

  /* App */
  .app { top: 1700px; height: 440px; }
  .phone-area { position: absolute; left: 270px; top: 60px; width: 230px; height: 340px; border-radius: 30px; background: linear-gradient(180deg, #e9ecee 0%, #e9ecee 12%, var(--teal) 14%, #1fa98a 86%, #dfe2e5 88%, #d8dbde 100%); }
  .app h2 { position: absolute; left: 600px; top: 112px; font-size: 44px; font-weight: 300; letter-spacing: 1px; }
  .app h2 b { font-weight: 900; }
  .app p { position: absolute; left: 600px; top: 180px; width: 500px; font-size: 19px; line-height: 28px; color: var(--muted); }
  .store-shape { position: absolute; left: 600px; top: 278px; width: 180px; height: 56px; background: linear-gradient(180deg, #5a6067, #3d4246); border-radius: 6px; }

  /* Footer */
  .footer { top: 2140px; height: 492px; background: var(--footer); color: var(--footer-text); }
  .newsletter h3 { position: absolute; left: 118px; top: 140px; color: var(--white); font-size: 22px; font-weight: 900; letter-spacing: 1px; }
  .newsletter p { position: absolute; left: 118px; top: 180px; width: 420px; font-size: 17px; line-height: 24px; }
  .newsletter .field { position: absolute; left: 118px; top: 244px; width: 420px; height: 52px; background: #4a4c4e; color: var(--footer-text); font-size: 19px; line-height: 52px; padding-left: 20px; }
  .subscribe { position: absolute; left: 420px; top: 316px; color: var(--white); font-size: 20px; font-weight: 700; }
  .subscribe .chev { margin-right: 8px; }
  .subscribe u { text-decoration: underline; }
  .col h4 { color: var(--white); font-size: 22px; font-weight: 700; margin-bottom: 6px; }
  .col ul { list-style: none; font-size: 15px; line-height: 20px; }
  .col { position: absolute; }
  .tutorials { left: 680px; top: 48px; }
  .articles { left: 860px; top: 48px; }
  .webtools { left: 860px; top: 116px; }
  .editor { left: 860px; top: 198px; }
  .editor h4 sup { font-size: 11px; font-weight: 400; margin-left: 4px; }
  .search { position: absolute; left: 680px; top: 316px; width: 460px; height: 44px; background: #4a4c4e; }
  .search svg { position: absolute; left: 14px; top: 11px; }
  .footer-bar { position: absolute; left: 0; bottom: 0; width: 1200px; height: 72px; background: var(--footer-bar); }
  .footer-links { position: absolute; right: 60px; top: 26px; display: flex; gap: 14px; list-style: none; font-size: 15px; color: #9a9c9e; }
</style>
</head>
<body>
  <header class="hero">
    <div class="hero-photo" role="img" aria-label="Photo of a person typing code on a laptop at a desk"></div>
    <div class="brand"><span class="brand-mark"></span>Brivanta</div>
    <ul class="nav">
      <li class="active">HOME</li><li>TUTORIALS</li><li>ARTICLES</li><li>WEBTOOLS</li><li>CONTACT</li>
    </ul>
    <h1 class="hero-title">A PLACE FOR LEARNING<br>AND TRYING OF ANY CODE.</h1>
    <span class="btn">GET STARTED</span>
  </header>

  <section class="tiles">
    <svg class="arrow prev" width="20" height="30" viewBox="0 0 20 30"><path d="M15 3 L4 15 L15 27" stroke="#8a8e92" stroke-width="4" fill="none"/></svg>
    <div class="tile html"><div class="tile-icon">&lt;/&gt;</div><div class="tile-label">HTML5</div></div>
    <div class="tile css"><div class="tile-icon">{ }</div><div class="tile-label">CSS</div></div>
    <div class="tile js"><div class="tile-icon">{;}</div><div class="tile-label">JAVASCRIPT</div></div>
    <div class="tile php"><div class="tile-icon">&lt;?&gt;</div><div class="tile-label">PHP</div></div>
    <div class="tile sql"><div class="tile-icon">[ ]</div><div class="tile-label">MySQL</div></div>
    <svg class="arrow next" width="20" height="30" viewBox="0 0 20 30"><path d="M5 3 L16 15 L5 27" stroke="#8a8e92" stroke-width="4" fill="none"/></svg>
  </section>

  <section class="welcome">
    <div class="laptop-area" role="img" aria-label="Illustration of a laptop showing a code editor"></div>
    <h2>WELCOME TO <b>BRIVANTA.</b></h2>
    <p>Brivanta is a place for Learning, testing, and examples for web building. The Examples in each chapter might be simplified to improve your basic understanding.</p>
    <span class="btn">KNOW MORE ABOUT US</span>
  </section>

  <section class="learn">
    <div class="then-line" style="left:400px;width:140px"></div>
    <div class="then-line" style="left:660px;width:60px"></div>
    <h2 class="left-title">LEARN</h2>
    <span class="then">then</span>
    <h2 class="right-title">PRACTICE</h2>
    <p class="left-copy">HTML, PHP, CSS, Javascripts, Jquery, XML, SQL, MySQL, etc.. All scripts are handy now. Start your course today, it's free.</p>
    <p class="right-copy">You will feel much easier than ever to learn about web programming languages including online code editor for each chapter, so you can edit, modify and execute the code.</p>
    <span class="btn red">GET ALL TUTORIALS</span>
    <span class="btn green">OPEN ONLINE EDITOR</span>
  </section>

  <section class="app">
    <div class="phone-area" role="img" aria-label="Illustration of a smartphone showing the mobile app"></div>
    <h2>LEARN <b>EVERYWHERE.</b></h2>
    <p>Get our Mobile App, and feel the freedom to learn anywhere, anytime you want. Get our Mobile App, and feel the freedom to learn anywhere, anytime you want.</p>
    <div class="store-shape" role="img" aria-label="App store download badge"></div>
  </section>

  <footer class="footer">
    <div class="newsletter">
      <h3>SUBSCRIBE TO OUR NEWSLETTER</h3>
      <p>Sign up for our newsletter and get the latest tutorials and updates.</p>
      <div class="field">youremail@example.com</div>
      <span class="subscribe"><span class="chev">›</span><u>Subscribe</u></span>
    </div>
    <div class="col tutorials">
      <h4>Tutorials</h4>
      <ul><li>HTML</li><li>CSS</li><li>JAVASCRIPT</li><li>PHP</li><li>SQL</li><li>JSON</li><li>MySQL</li><li>Regex</li><li>RSS</li></ul>
    </div>
    <div class="col articles"><h4>Articles</h4></div>
    <div class="col webtools">
      <h4>Webtools</h4>
      <ul><li>CSS minifier</li><li>JAVASCRIPT minifier</li></ul>
    </div>
    <div class="col editor"><h4>Online Code Editor<sup>BETA</sup></h4></div>
    <div class="search">
      <svg width="22" height="22" viewBox="0 0 22 22"><circle cx="9" cy="9" r="6" stroke="#c9cbcd" stroke-width="2.5" fill="none"/><path d="M13.5 13.5 L19 19" stroke="#c9cbcd" stroke-width="2.5"/></svg>
    </div>
    <div class="footer-bar">
      <ul class="footer-links"><li>About</li><li>/</li><li>Terms</li><li>/</li><li>Privacy</li><li>/</li><li>Disclaimer</li><li>/</li><li>Contact</li><li>/</li><li>FAQ</li></ul>
    </div>
  </footer>
</body>
</html>
```